Commercial Real Estate website

Need a web design commercial real estate company specializing in retail shopping centers based in Orlando, FL. We would like pictures of Orlando city skyline with hues and colors that go with hot pink. We want to stress the relationship of time on the value of real estate.
It should gave a rotating page that highlights our property listings.

Target Market(s)

Owners of shopping centers and national retail tenants looking for tenant representatives.

Industry/Entity Type

Real Estate

Number of Pages Required

5+ page

Font styles to use
Serif

Colors
e34197

Requirements
Must have
• Pictures of commercial retail grocery anchored shopping centers and city scapes and skylines.

```html
<!DOCTYPE html>
<html lang="en">
<head>
<meta charset="utf-8">
<title>Clockwise Commercial</title>
<link href="https://fonts.googleapis.com/css2?family=Open+Sans:wght@400;600;700;800&display=swap" rel="stylesheet">
<style>
:root{
  --pink:#e34197;
  --pink-dark:#c92f80;
  --ink:#333840;
  --muted:#8a8f96;
  --line:#e3e4e7;
  --paper:#ffffff;
  --soft:#f2f2f4;
  --night:#1c2540;
  --footer-dark:#2a2d33;
}
*{margin:0;padding:0;box-sizing:border-box}
html,body{width:1200px;height:2616px;overflow:hidden}
body{font-family:"Open Sans",Arial,sans-serif;color:var(--ink);background:var(--paper);position:relative}
.abs{position:absolute}

/* header + hero */
.hero{left:0;top:0;width:1200px;height:540px;background:linear-gradient(180deg,#2b2f5c 0%,#5b4c86 35%,#3b5e8f 62%,#1d3558 100%)}
.logo{left:100px;top:40px;color:#fff;font-size:30px;font-weight:600;display:flex;align-items:center;gap:12px;letter-spacing:.5px}
.logo .dot{width:14px;height:14px;border-radius:50%;background:#fff}
.nav{right:96px;top:40px;display:flex;gap:6px}
.nav a{color:#fff;text-decoration:none;font-size:13px;font-weight:600;padding:10px 14px;letter-spacing:.5px}
.nav a.active{border:1px solid #fff}
.hero-title{left:0;width:1200px;top:270px;text-align:center;color:#fff;font-size:54px;font-weight:800;letter-spacing:1px}
.hero-sub{left:350px;width:500px;top:352px;text-align:center;color:#e8e6f2;font-size:14px;line-height:22px}
.arrow{top:280px;width:30px;height:40px}

/* services band */
.band{left:0;top:540px;width:1200px;height:320px;background:var(--pink)}
.service{top:520px;width:300px;text-align:center;color:#fff}
.service .icon{width:120px;height:120px;margin:0 auto;border-radius:50%;background:#8d8f96;border:6px solid #fff;display:flex;align-items:center;justify-content:center}
.service h3{font-size:18px;font-weight:600;margin-top:36px;letter-spacing:.5px}
.service p{font-size:13px;line-height:20px;margin:12px 30px 0;color:#fde7f2}
.btn-dark{display:inline-block;background:#3b3e46;color:#fff;font-size:11px;font-weight:700;padding:9px 20px;letter-spacing:.5px}
.service .btn-dark{margin-top:22px}

/* listings */
.section-title{left:0;width:1200px;text-align:center;font-size:30px;font-weight:700;letter-spacing:1px}
.section-title span{color:var(--pink)}
.title-rule{left:560px;width:80px;height:2px;background:var(--pink)}
.card{top:990px;width:228px;height:390px;background:var(--soft);overflow:hidden}
.card .photo{width:228px;height:172px}
.card h4{font-size:12px;font-weight:700;margin:14px 14px 0;text-transform:uppercase;white-space:nowrap}
.card .price{color:var(--pink);font-size:18px;font-weight:700;margin:10px 14px 0}
.card p{font-size:12px;line-height:18px;color:var(--muted);margin:8px 14px 0}
.card .btn-dark{margin:18px 14px 0}
.dots{left:0;width:1200px;top:1412px;display:flex;justify-content:center;gap:10px}
.dots i{width:12px;height:12px;border-radius:50%;background:#b9bcc2}
.dots i.on{background:var(--pink)}

/* about */
.about{left:0;top:1470px;width:1200px;height:430px;background:var(--soft)}
.portrait{left:110px;top:1505px;width:220px;height:395px;background:linear-gradient(180deg,#dfe3ea 0%,#aeb9c9 50%,#5d6f8e 100%)}
.about-text{left:360px;top:1530px;width:440px}
.about-text .kicker{font-size:24px;font-weight:600;color:var(--ink)}
.about-text h2{font-size:28px;font-weight:800;margin-top:4px;white-space:nowrap}
.about-text .rule{width:70px;height:2px;background:var(--pink);margin:16px 0 20px}
.about-text p{font-size:13px;line-height:21px;color:var(--muted);margin-bottom:14px;width:400px}
.about-text .btn-dark{margin-top:10px;padding:11px 22px}
.form{left:820px;top:1505px;width:280px}
.form h3{font-size:20px;font-weight:600;letter-spacing:1px}
.form .rule{width:60px;height:2px;background:var(--pink);margin:12px 0 18px}
.field{height:40px;background:#fff;border:1px solid var(--line);margin-bottom:14px;font-size:12px;color:#a3a7ad;padding:12px 14px}
.field.tall{height:60px}
.btn-pink{display:inline-block;background:var(--pink);color:#fff;font-size:12px;font-weight:700;padding:12px 22px;letter-spacing:.5px}

/* news */
.news-title{left:100px;top:1935px;font-size:24px;font-weight:700;letter-spacing:.5px}
.news-rule{left:100px;top:1974px;width:70px;height:2px;background:var(--pink)}
.news-item{left:100px;width:540px;display:flex;gap:24px}
.news-item .photo{width:220px;height:130px;flex:none}
.news-item h4{font-size:13px;font-weight:700;margin-top:6px}
.news-item .date{color:var(--pink);font-size:12px;font-weight:600;margin-top:6px}
.news-item p{font-size:12px;line-height:18px;color:var(--muted);margin-top:8px}
.news-item .more{font-size:11px;font-weight:700;margin-top:10px}
.video{left:690px;top:1960px;width:410px;height:270px;background:linear-gradient(160deg,#3c4150 0%,#22252e 100%)}
.video-bar{left:690px;top:2230px;width:410px;height:30px;background:#1a1c22}

/* footer */
.footer{left:0;top:2320px;width:1200px;height:232px;background:var(--pink);color:#fff}
.col{top:2350px}
.col h5{font-size:14px;font-weight:700;letter-spacing:.5px}
.col .rule{width:40px;height:2px;background:#fff;margin:10px 0 14px}
.col p,.col li{font-size:12px;line-height:22px;color:#fde7f2;list-style:none}
.col li::before{content:"› ";}
.signup{display:flex;margin-top:12px}
.signup .in{width:150px;height:36px;background:#fff;color:#a3a7ad;font-size:12px;padding:10px}
.signup .go{height:36px;background:#3b3e46;color:#fff;font-size:11px;font-weight:700;padding:11px 14px}
.contact-row{display:flex;align-items:center;gap:8px;font-size:12px;line-height:24px;color:#fde7f2}
.social{display:flex;gap:8px;margin-top:10px}
.social i{width:24px;height:24px;border:1px solid #fff;border-radius:50%}
.bottom{left:0;top:2552px;width:1200px;height:64px;background:var(--footer-dark);color:#9a9ea6;font-size:12px}
.bottom .left{position:absolute;left:100px;top:24px}
.bottom .right{position:absolute;right:100px;top:24px}
</style>
</head>
<body>

<div class="abs hero" role="img" aria-label="Orlando city skyline at dusk with lit towers reflected in the lake"></div>
<div class="abs logo"><span class="dot"></span>Clockwise Commercial</div>
<nav class="abs nav">
  <a class="active">HOME</a><a>ABOUT US</a><a>PROPERTY LISTING</a><a>SERVICES</a><a>NEWS</a><a>CONTACT US</a>
</nav>
<svg class="abs arrow" style="left:20px" viewBox="0 0 30 40"><path d="M20 6 8 20l12 14" fill="none" stroke="#fff" stroke-width="3"/></svg>
<svg class="abs arrow" style="right:20px" viewBox="0 0 30 40"><path d="M10 6l12 14-12 14" fill="none" stroke="#fff" stroke-width="3"/></svg>
<h1 class="abs hero-title">CLOCKWISE COMMERCIAL</h1>
<p class="abs hero-sub">Trusted guidance for retail centers across central Florida, where every hour shapes the value of the property you hold.</p>

<div class="abs band"></div>
<div class="abs service" style="left:110px">
  <div class="icon"><svg width="50" height="56" viewBox="0 0 50 56"><rect x="10" y="4" width="30" height="48" fill="none" stroke="#fff" stroke-width="3"/><path d="M17 12h6M27 12h6M17 20h6M27 20h6M17 28h6M27 28h6M17 36h6M27 36h6" stroke="#fff" stroke-width="3"/><rect x="21" y="42" width="8" height="10" fill="#fff"/></svg></div>
  <h3>COMMERCIAL</h3>
  <p>Leasing and sales advice for office, flex and industrial space with clear market data behind each step.</p>
  <span class="btn-dark">READ MORE</span>
</div>
<div class="abs service" style="left:450px">
  <div class="icon"><svg width="56" height="52" viewBox="0 0 56 52"><path d="M4 26 28 6l24 20" fill="none" stroke="#fff" stroke-width="3"/><path d="M11 22v26h34V22" fill="none" stroke="#fff" stroke-width="3"/><rect x="23" y="32" width="10" height="16" fill="#fff"/></svg></div>
  <h3>RESIDENTIAL</h3>
  <p>Homes, condos and multi-family assets priced with care and matched to buyers who are ready to move.</p>
  <span class="btn-dark">READ MORE</span>
</div>
<div class="abs service" style="left:790px">
  <div class="icon"><svg width="56" height="50" viewBox="0 0 56 50"><path d="M3 6h9l6 26h28l5-18H15" fill="none" stroke="#fff" stroke-width="3" stroke-linejoin="round"/><circle cx="21" cy="42" r="4" fill="#fff"/><circle cx="42" cy="42" r="4" fill="#fff"/></svg></div>
  <h3>RETAIL SHOPPING</h3>
  <p>Grocery anchored centers and national tenants brought together through focused tenant representation work.</p>
  <span class="btn-dark">READ MORE</span>
</div>

<h2 class="abs section-title" style="top:908px">OUR <span>PROPERTY</span> LISTINGS</h2>
<div class="abs title-rule" style="top:958px"></div>

<div class="abs card" style="left:100px">
  <div class="photo" role="img" aria-label="Glass office towers against a blue sky" style="background:linear-gradient(180deg,#8fb6dc,#5b7f9f)"></div>
  <h4>Lake Nona Retail Plaza</h4><div class="price">$ 115,000</div>
  <p>Anchored retail center with strong daily traffic and long term tenants in place.</p>
  <span class="btn-dark">READ MORE</span>
</div>
<div class="abs card" style="left:357px">
  <div class="photo" role="img" aria-label="Modern commercial buildings at street level" style="background:linear-gradient(180deg,#a8c4de,#6d8597)"></div>
  <h4>Colonial Drive Center</h4><div class="price">$ 115,000</div>
  <p>Anchored retail center with strong daily traffic and long term tenants in place.</p>
  <span class="btn-dark">READ MORE</span>
</div>
<div class="abs card" style="left:614px">
  <div class="photo" role="img" aria-label="City skyline with high rise towers" style="background:linear-gradient(180deg,#6f9ed0,#44698c)"></div>
  <h4>Downtown Office Tower</h4><div class="price">$ 115,000</div>
  <p>Anchored retail center with strong daily traffic and long term tenants in place.</p>
  <span class="btn-dark">READ MORE</span>
</div>
<div class="abs card" style="left:872px">
  <div class="photo" role="img" aria-label="Tall residential and office towers under a clear sky" style="background:linear-gradient(180deg,#9cc3e8,#587a99)"></div>
  <h4>Winter Park Marketplace</h4><div class="price">$ 115,000</div>
  <p>Anchored retail center with strong daily traffic and long term tenants in place.</p>
  <span class="btn-dark">READ MORE</span>
</div>
<div class="abs dots"><i class="on"></i><i></i><i></i><i></i></div>

<div class="abs about"></div>
<div class="abs portrait" role="img" aria-label="Smiling businessman in a white shirt and tie, arms crossed"></div>
<div class="abs about-text">
  <div class="kicker">WELCOME TO</div>
  <h2>CLOCKWISE COMMERCIAL</h2>
  <div class="rule"></div>
  <p>We have worked with owners and tenants across Orlando for years, and we know that timing decides the deal.</p>
  <p>From first tour to signed lease, our team keeps each project moving on schedule and on budget.</p>
  <span class="btn-dark">READ MORE &nbsp;›</span>
</div>
<div class="abs form">
  <h3>GET IN TOUCH</h3>
  <div class="rule"></div>
  <div class="field">Name</div>
  <div class="field">E-mail</div>
  <div class="field">Phone No</div>
  <div class="field tall">Comments</div>
  <span class="btn-pink">SUBMIT ENQUIRY</span>
</div>

<h2 class="abs news-title">LATEST NEWS</h2>
<div class="abs news-rule"></div>
<div class="abs news-item" style="top:1995px">
  <div class="photo" role="img" aria-label="Multi-storey commercial building exterior" style="background:linear-gradient(180deg,#b7cde3,#7d8e9e)"></div>
  <div><h4>NEW CENTER OPENS IN SOUTH ORLANDO</h4><div class="date">JULY 20, 2016</div>
  <p>Leasing is now open for a new grocery anchored center with space for local and national shops.</p><div class="more">LEARN MORE</div></div>
</div>
<div class="abs news-item" style="top:2150px">
  <div class="photo" role="img" aria-label="Large modern office building at dusk" style="background:linear-gradient(180deg,#c9b89f,#6e6a70)"></div>
  <div><h4>MARKET REPORT FOR THE THIRD QUARTER</h4><div class="date">JUNE 14, 2016</div>
  <p>Leasing is now open for a new grocery anchored center with space for local and national shops.</p><div class="more">LEARN MORE</div></div>
</div>
<div class="abs video" role="img" aria-label="Company introduction video"></div>
<svg class="abs" style="left:865px;top:2065px" width="60" height="60" viewBox="0 0 60 60"><circle cx="30" cy="30" r="28" fill="var(--pink)"/><path d="M24 18l18 12-18 12z" fill="#fff"/></svg>
<div class="abs video-bar"></div>
<div class="abs" style="left:740px;top:2244px;width:300px;height:3px;background:#4a4e58"></div>
<div class="abs" style="left:740px;top:2244px;width:60px;height:3px;background:var(--pink)"></div>

<div class="abs footer"></div>
<div class="abs col" style="left:100px;width:240px">
  <h5>SIGN UP TO RECEIVE EMAIL</h5><div class="rule"></div>
  <p>Get our latest listings and market news sent straight to your inbox.</p>
  <div class="signup"><div class="in">Enter email</div><div class="go">SUBSCRIBE</div></div>
</div>
<div class="abs col" style="left:400px">
  <h5>FEATURED SERVICES</h5><div class="rule"></div>
  <ul><li>Residential</li><li>Commercial</li><li>Retail Shopping</li><li>Industry</li></ul>
</div>
<div class="abs col" style="left:620px">
  <h5>QUICK LINKS</h5><div class="rule"></div>
  <ul><li>Support</li><li>Our Account</li><li>About Us</li><li>Terms of use</li></ul>
</div>
<div class="abs col" style="left:860px">
  <h5>CONTACT US</h5><div class="rule"></div>
  <div class="contact-row"><svg width="12" height="16" viewBox="0 0 12 16"><path d="M6 1a5 5 0 0 0-5 5c0 4 5 9 5 9s5-5 5-9a5 5 0 0 0-5-5z" fill="#fff"/></svg>P.O. Box 1234, Orlando, FL 32801</div>
  <div class="contact-row"><svg width="12" height="14" viewBox="0 0 12 14"><path d="M2 1h3l1 3-2 1a8 8 0 0 0 4 4l1-2 3 1v3c0 1-1 2-2 2A10 10 0 0 1 1 3c0-1 0-2 1-2z" fill="#fff"/></svg>+1 407 555 0142</div>
  <div class="contact-row"><svg width="14" height="10" viewBox="0 0 14 10"><rect x="0.5" y="0.5" width="13" height="9" fill="none" stroke="#fff"/><path d="M1 1l6 5 6-5" fill="none" stroke="#fff"/></svg>info@clockwisecommercial.com</div>
  <div class="social"><i></i><i></i><i></i><i></i></div>
</div>
<div class="abs bottom">
  <span class="left">© 2016 Clockwise Commercial. All Rights Reserved.</span>
  <span class="right">Terms of Service | Privacy Policy</span>
</div>

</body>
</html>
```